Harborlight Capital Estates business card

We are a real estate advisory and investment company. We are specialized in assisting high networth individuals to invest in real estate overseas. We deliver a very personalized service, anticipating all the potential challenges an investor can face, and making it easy and safe for them. We also co-invest with our clients, assuring them that each project will be looked after as it is our own, and at the same time giving them the extra booth on confidence to invest.

We need a business card design. The business card must have a very premium, high-end look, reflecting principles like "commitment", "trust" and "timeless (but contemporary)". We look for long term relationships with our clients, and we grow with their referrals. We are all about conquering the confidence of the clients by always delivering above the expectations performance.

Target Market(s)

High net worth individuals.

Industry/Entity Type

Real Estate

Contact Information for Business Card

Please consider places on the business card for:

Name
Function (bellow name in smaller size text)

Mobile phone
E-mail
Skype ID
WeChat ID

Adress (3 lines)

Also include the following locations references:
PORTUGAL * DUBAI * HONG KONG

Website: www.hcestates-example.com

Requirements
Must have
• Company Logo

```html
<!DOCTYPE html>
<html lang="en">
<head>
<meta charset="UTF-8">
<title>Harborlight Capital Estates – Business Card</title>
<link href="https://fonts.googleapis.com/css2?family=Open+Sans:wght@400;600;700&display=swap" rel="stylesheet">
<style>
  :root {
    --stage: #000000;
    --sky: #29aae1;
    --slate: #858688;
    --white: #ffffff;
  }
  * { margin: 0; padding: 0; box-sizing: border-box; }
  html, body {
    width: 1200px; height: 900px; overflow: hidden;
    background: var(--stage);
    font-family: "Open Sans", Arial, sans-serif;
    color: var(--white);
  }
  .canvas { position: relative; width: 1200px; height: 900px; }

  .card { position: absolute; top: 275px; width: 477px; height: 293px; overflow: hidden; }
  .card--front { left: 116px; background: var(--sky); border-radius: 0 46px 0 46px; }
  .card--back { left: 622px; background: var(--slate); border-radius: 46px 0 46px 0; }

  .brand {
    position: absolute; font-weight: 600; text-transform: uppercase;
    letter-spacing: 2px; line-height: 1.2;
  }
  .card--front .brand { left: 31px; top: 70px; font-size: 21px; color: var(--white); }
  .card--back .brand {
    left: 0; right: 0; top: 126px; text-align: center;
    font-size: 22px; color: var(--sky);
  }
  .brand-mark {
    display: inline-block; width: 12px; height: 12px; border-radius: 50%;
    background: currentColor; margin-right: 8px; vertical-align: 2px;
  }

  .person { position: absolute; right: 23px; top: 47px; text-align: right; }
  .person-name { font-size: 17px; font-weight: 700; line-height: 1.2; }
  .person-role { font-size: 13px; line-height: 1.4; }

  .address { position: absolute; left: 31px; top: 205px; font-size: 13px; line-height: 14.5px; }

  .contacts { position: absolute; right: 24px; top: 182px; list-style: none; }
  .contacts li {
    display: flex; justify-content: flex-end; align-items: center;
    height: 20px; font-size: 13px;
  }
  .contacts svg { width: 12px; height: 12px; margin-left: 7px; fill: var(--white); }

  .locations {
    position: absolute; left: 0; right: 0; top: 201px; text-align: center;
    font-size: 13px; font-weight: 700; text-decoration: underline;
  }
  .web-band {
    position: absolute; left: 0; right: 0; top: 242px; height: 34px;
    background: var(--sky); display: flex; align-items: center; justify-content: center;
    font-size: 13px; font-weight: 700; text-decoration: underline;
  }
</style>
</head>
<body>
<div class="canvas">
  <section class="card card--front">
    <div class="brand"><span class="brand-mark"></span>Harborlight<br>Capital Estates</div>

    <div class="person">
      <div class="person-name">Daniel Marlow</div>
      <div class="person-role">Managing Director</div>
    </div>

    <div class="address">12345, Address<br>Goes Here Country<br>Name, 123456</div>

    <ul class="contacts">
      <li>(044)-456-7890
        <svg viewBox="0 0 24 24"><path d="M6.6 10.8a15.1 15.1 0 0 0 6.6 6.6l2.2-2.2c.3-.3.7-.4 1-.2 1.1.4 2.3.6 3.6.6.6 0 1 .4 1 1V20c0 .6-.4 1-1 1A17 17 0 0 1 3 4c0-.6.4-1 1-1h3.5c.6 0 1 .4 1 1 0 1.3.2 2.5.6 3.6.1.3 0 .7-.2 1z"/></svg>
      </li>
      <li>123-456-7890
        <svg viewBox="0 0 24 24"><path d="M2 5h20v14H2z M2 5l10 8 10-8" fill="none" stroke="#fff" stroke-width="2"/><path d="M2 5h20l-10 8z"/></svg>
      </li>
      <li>/yourname.com
        <svg viewBox="0 0 24 24"><circle cx="12" cy="12" r="10"/></svg>
      </li>
      <li>/yourname.com
        <svg viewBox="0 0 24 24"><circle cx="12" cy="12" r="10"/></svg>
      </li>
    </ul>
  </section>

  <section class="card card--back">
    <div class="brand"><span class="brand-mark"></span>Harborlight Capital Estates</div>
    <div class="locations">PORTUGAL * DUBAI * HONG KONG</div>
    <div class="web-band">www.hcestates-example.com</div>
  </section>
</div>
</body>
</html>
```